Identification Supplier website

Front and product page designs required for this Business Catalyst website for an identification supply company.

Also interested in coding same into finished site for additional fee.

Client is a security/event ID supplies company selling identification products like card holders, printers, lanyards, clips and so on.

Current placeholder site is at:
http://www.markovatel.com.au/

Other sites the client likes are at:

www.brantovagoods.com.au

www.tagwarely.com.au

www.rvb.com.au

http://start42.veldrana.co.nz/online/welcome.csn

Otherwise colour scheme should follow logo and structure should follow wireframe attached.

```html
<!DOCTYPE html>
<html lang="en">
<head>
<meta charset="utf-8">
<title>markovatel – ID Systems, Supplies, Services and Accessories</title>
<link rel="stylesheet" href="https://fonts.googleapis.com/css2?family=Arimo:wght@400;700&family=Crimson+Pro:ital@1&display=swap">
<style>
:root{
  --page-bg:#d5e8f0;
  --white:#ffffff;
  --brand-blue:#3463b0;
  --accent-blue:#1a9bd7;
  --navy:#1f3b73;
  --text:#222222;
  --muted:#555555;
  --tile-head:#eeeeee;
  --tile-border:#dddddd;
  --panel-light:#e8f1f7;
  --panel-dark:#333333;
}
*{margin:0;padding:0;box-sizing:border-box}
html,body{width:1200px;height:959px;overflow:hidden}
body{background:var(--page-bg);font-family:"Arimo",Arial,sans-serif;color:var(--text);position:relative}
.site{position:absolute;left:109px;top:0;width:983px;height:959px;background:var(--white)}
.abs{position:absolute}
.topbar{left:0;top:0;width:983px;height:24px;background:var(--brand-blue);color:var(--white);font-size:12px;text-align:right;padding:5px 13px 0 0}
.topbar a{color:var(--white);text-decoration:none}
.brand{left:11px;top:40px;display:flex;align-items:center;gap:10px}
.brand-mark{width:34px;height:34px;border-radius:50%;background:var(--brand-blue)}
.brand-name{font-size:44px;color:var(--navy);font-weight:400;letter-spacing:-0.5px}
.tagline{left:302px;top:38px;font-family:"Crimson Pro",Georgia,serif;font-style:italic;font-size:25px;color:var(--text)}
.nav{left:500px;top:84px;display:flex;font-size:12px}
.nav a{display:block;height:28px;line-height:28px;padding:0 12px;color:var(--text);text-decoration:none;border-radius:2px}
.nav a.current{background:var(--accent-blue);color:var(--white);width:62px;text-align:center;margin-right:0}
.hero{left:11px;top:138px;width:680px;height:270px;background:var(--brand-blue);overflow:hidden}
.hero-title{left:24px;top:66px;color:var(--white);font-size:23px;line-height:30px}
.hero-title span{display:block;padding-left:72px}
.hero-copy{left:26px;top:154px;width:275px;color:var(--white);font-size:14px;line-height:18px;text-align:justify}
.hero-photo{left:300px;top:0;width:380px;height:270px;background:linear-gradient(90deg,rgba(52,99,176,0) 0%,#b9c6dc 35%,#dfe4ec 70%,#9fb0cc 100%)}
.tile{width:165px;height:183px;border:1px solid var(--tile-border)}
.tile-head{height:46px;background:var(--tile-head);display:flex;align-items:center;justify-content:center;text-align:center;font-size:14px;line-height:17px;color:var(--text)}
.tile-photo{height:135px}
.whats-new{left:741px;top:138px;width:230px;height:270px;background:var(--panel-light);padding:10px 12px}
.panel-title{font-size:20px;color:var(--brand-blue)}
.news-item{margin-top:26px;font-size:12px;line-height:14px;color:var(--muted)}
.news-item:first-of-type{margin-top:27px}
.news-item b{color:#444;letter-spacing:0.3px}
.read-more{position:absolute;right:12px;bottom:7px;font-size:12px;color:var(--brand-blue);text-decoration:none}
.newsletter{left:741px;top:426px;width:230px;height:177px;background:var(--panel-dark);color:var(--white);padding:10px 12px}
.newsletter .panel-title{color:var(--white)}
.newsletter p{font-size:12.5px;line-height:15px;margin-top:10px;letter-spacing:0.2px}
.email{display:block;margin-top:10px;width:199px;height:30px;border:1px solid #aaa;border-radius:4px;background:var(--white);font:13px "Arimo",Arial,sans-serif;padding:0 10px;color:var(--text)}
.signup{position:absolute;right:19px;top:132px;width:72px;height:29px;background:var(--accent-blue);color:var(--white);border:0;border-radius:3px;font:14px "Arimo",Arial,sans-serif}
.featured{left:741px;top:620px;width:230px;height:226px;background:var(--panel-light);padding:7px 11px}
.featured-photo{margin-top:6px;width:208px;height:148px;border:1px solid #b7dbe8;background:radial-gradient(circle at 50% 50%,#c9cacc 0%,#8d8f93 45%,#ffffff 72%)}
.featured p{font-size:12px;line-height:14px;margin-top:7px;padding-left:2px}
.footer{left:0;top:900px;width:983px;height:59px;background:var(--brand-blue);color:var(--white);text-align:center;font-size:12px;line-height:22px;padding-top:7px}
.footer a{color:var(--white);text-decoration:none}
</style>
</head>
<body>
<div class="site">
  <div class="abs topbar"><a href="#">Order Now</a>&nbsp;&nbsp;|&nbsp;&nbsp;<a href="#">Login</a></div>

  <div class="abs brand"><span class="brand-mark"></span><span class="brand-name">markovatel</span></div>
  <div class="abs tagline">ID Systems, Supplies, Services and Accessories</div>

  <nav class="abs nav">
    <a class="current" href="#">Home</a>
    <a href="#">About Us</a>
    <a href="#">Our Products</a>
    <a href="#">Our Services</a>
    <a href="#">News</a>
    <a href="#">Contact Us</a>
  </nav>

  <section class="abs hero">
    <div class="abs hero-photo" role="img" aria-label="ID card printer with printed cards fanned in front"></div>
    <h1 class="abs hero-title" style="font-weight:400">Lorem ipsum dolor sit amet<span>consectetur adipiscing elit</span></h1>
    <p class="abs hero-copy">Lorem ipsum dolor sit amet, consectetur adipiscing elit. Morbi luctus sagittis sapien, nec pharetra neque porttitor in.</p>
  </section>

  <div class="abs tile" style="left:11px;top:446px"><div class="tile-head">Card Printers<br>And Ribbons</div><div class="tile-photo" role="img" aria-label="Card printer with ribbon cartridge" style="background:linear-gradient(135deg,#e8eef2,#4bb0d8 55%,#f2f4f6)"></div></div>
  <div class="abs tile" style="left:183px;top:446px"><div class="tile-head">Solutions</div><div class="tile-photo" role="img" aria-label="Sample photo ID cards" style="background:linear-gradient(135deg,#f4f6f8,#3a6fb4 55%,#f4f6f8)"></div></div>
  <div class="abs tile" style="left:354px;top:446px"><div class="tile-head">Bureau Services</div><div class="tile-photo" role="img" aria-label="Stack of printed plastic cards" style="background:linear-gradient(160deg,#ffffff 20%,#6aa4d6 55%,#e9b64a 75%,#ffffff)"></div></div>
  <div class="abs tile" style="left:526px;top:446px"><div class="tile-head">Laminates</div><div class="tile-photo" role="img" aria-label="Holographic laminate over an ID card" style="background:linear-gradient(135deg,#f6f0f2,#d7b8c4 50%,#f0e6d8)"></div></div>

  <div class="abs tile" style="left:11px;top:661px"><div class="tile-head">Lanyards</div><div class="tile-photo" role="img" aria-label="Assorted printed lanyards" style="background:linear-gradient(135deg,#ffffff,#e94f3c 35%,#f3c322 55%,#49b04c 75%,#ffffff)"></div></div>
  <div class="abs tile" style="left:183px;top:661px"><div class="tile-head">Wristbands</div><div class="tile-photo" role="img" aria-label="Printed silicone wristbands" style="background:radial-gradient(circle,#f08a2a 0%,#d93636 35%,#2e6fc2 60%,#ffffff 78%)"></div></div>
  <div class="abs tile" style="left:354px;top:661px"><div class="tile-head">Card Holders</div><div class="tile-photo" role="img" aria-label="Clear plastic card holders" style="background:linear-gradient(135deg,#ffffff,#dfe6ee 50%,#ffffff)"></div></div>
  <div class="abs tile" style="left:526px;top:661px"><div class="tile-head">Accessories</div><div class="tile-photo" role="img" aria-label="Badge reels, clips and pins" style="background:linear-gradient(135deg,#f2f2f2,#6fbf4a 45%,#8a8a8a 70%,#3fae3f)"></div></div>

  <aside class="abs whats-new">
    <h2 class="panel-title" style="font-weight:400">Whats New</h2>
    <p class="news-item"><b>Lorem ipsum dolor sit amet,</b><br>Consectetur adipiscing elit. Vivamus<br>&nbsp;quis turpis dapibus.</p>
    <p class="news-item"><b>Lorem ipsum dolor sit amet,</b><br>Consectetur adipiscing elit. Vivamus<br>&nbsp;quis turpis dapibus.</p>
    <p class="news-item"><b>Lorem ipsum dolor sit amet,</b><br>Consectetur adipiscing elit. Vivamus<br>&nbsp;quis turpis dapibus.</p>
    <a class="read-more" href="#">Read More &gt;</a>
  </aside>

  <aside class="abs newsletter">
    <h2 class="panel-title" style="font-weight:400">Newsletter Signup</h2>
    <p>Enter your email address below to recieve our monthly newsletter.</p>
    <input class="email" type="text" placeholder="Email address" aria-label="Email address">
    <button class="signup" type="button">Signup</button>
  </aside>

  <aside class="abs featured">
    <h2 class="panel-title" style="font-weight:400">Featured Products</h2>
    <div class="featured-photo" role="img" aria-label="Grey desktop card printer"></div>
    <p>Lorem ipsum dolor sit amet, consectet adipiscing elit.</p>
  </aside>

  <footer class="abs footer">
    Copyright © 2013 markovatel. All Rights Reserved.<br>
    <a href="#">Terms &amp; Conditions</a> | <a href="#">Privacy Policy</a>
  </footer>
</div>
</body>
</html>
```